Velstrand Business Card - Construction Management

Create a business card for a construction management firm that owns/responsible for three other companies and include the following:
Main Company & Logo - Velstrand Holdings Group Ltd.
Subsidiary Company Logo only to appear on card in miniature form :
Tallec Fabrication Services Ltd.
Halvard Sisters Building Inc.
Copperline Civilworks

Contact Information for Business Card

Velstrand Holdings Group Ltd.
482 Tovey Lane - Lindqvist Commerce Park
RM of Brackett
Regina, Saskatchewan
S7J 2B9
P: 306.555.0182
C: 306.555.0147
e:jtoverud@velstrand.ca

Colors

Designer to choose colors to be used in the design.

Requirements
Must have
• Main Logo and small/miniature version of three subsidiary company logos.
• We would appreciate seeing a version of main logo(Velstrand Group) on front of card and other three miniature/small logos on the front of the card or version of main logo on front and other three logos on the back of the card.

```html
<!DOCTYPE html>
<html lang="en">
<head>
<meta charset="utf-8">
<title>Velstrand Group – Business Card</title>
<link rel="stylesheet" href="https://fonts.googleapis.com/css2?family=Montserrat:wght@500;600;800&display=swap">
<style>
  :root {
    --backdrop: #4a4b4e;
    --card-white: #ffffff;
    --card-black: #141414;
    --card-black-edge: #262626;
    --brand-blue: #1a6fc4;
    --brand-grey: #7d7f82;
    --ink: #1c1c1c;
    --copper: #2b73b8;
    --halvard-red: #c8202e;
    --tallec-brown: #5b1d1f;
  }
  * { box-sizing: border-box; margin: 0; padding: 0; }
  html, body {
    width: 1200px; height: 1000px; overflow: hidden;
    background: radial-gradient(ellipse at 50% 35%, #5c5d60 0%, var(--backdrop) 60%, #37383a 100%);
    font-family: "Montserrat", Arial, sans-serif;
  }
  .card {
    position: absolute;
    width: 600px; height: 343px;
    border-radius: 22px;
    box-shadow: 0 18px 40px rgba(0,0,0,.45);
    overflow: hidden;
  }
  /* Back side */
  .card-back { left: 500px; top: 60px; background: var(--card-black); }
  .back-texture {
    position: absolute; inset: 0;
    background: radial-gradient(circle at 50% 45%, var(--card-black-edge) 0%, var(--card-black) 70%);
  }
  .back-mark {
    position: absolute; left: 50%; top: 50%;
    transform: translate(-50%, -50%);
    display: flex; align-items: center; gap: 12px;
    font-weight: 800; font-size: 30px; letter-spacing: 1px;
    color: var(--brand-blue);
  }
  .back-mark .mark-square { width: 26px; height: 26px; background: var(--brand-blue); }

  /* Front side */
  .card-front { left: 100px; top: 440px; background: var(--card-white); }
  .brand-block {
    position: absolute; left: 40px; top: 110px;
    display: flex; align-items: center; gap: 14px;
  }
  .brand-block .mark-square { width: 52px; height: 52px; background: var(--brand-blue); flex: none; }
  .brand-name {
    font-weight: 800; font-size: 28px; line-height: 1.05; letter-spacing: .5px;
    color: var(--brand-blue); text-transform: uppercase;
  }
  .divider {
    position: absolute; left: 322px; top: 70px;
    width: 2px; height: 190px; background: var(--brand-blue);
  }
  .contact {
    position: absolute; left: 342px; top: 74px; width: 240px;
    color: var(--ink);
  }
  .contact .person {
    font-weight: 800; font-size: 19px; color: var(--brand-blue);
    text-transform: uppercase; letter-spacing: .3px;
  }
  .contact .role { font-weight: 500; font-size: 13px; margin-top: 2px; }
  .contact address {
    font-style: normal; font-weight: 600; font-size: 13px; line-height: 1.25;
    margin-top: 16px;
  }
  .contact ul { list-style: none; margin-top: 8px; }
  .contact li {
    display: flex; align-items: center; gap: 8px;
    font-weight: 600; font-size: 13.5px; line-height: 1.45;
  }
  .contact li svg { width: 13px; height: 13px; flex: none; fill: var(--brand-blue); }
  .contact .web-accent { color: var(--brand-blue); }
  .subsidiaries {
    position: absolute; left: 0; right: 0; bottom: 30px;
    display: flex; justify-content: center; align-items: center; gap: 48px;
    font-weight: 800; font-size: 11px; text-transform: uppercase; letter-spacing: .3px;
  }
  .subsidiary { display: flex; align-items: center; gap: 6px; }
  .subsidiary .dot { width: 14px; height: 14px; border-radius: 50%; }
  .sub-copperline { color: var(--copper); }
  .sub-copperline .dot { background: var(--copper); }
  .sub-halvard { color: var(--ink); }
  .sub-halvard .dot { background: var(--halvard-red); border-radius: 0; }
  .sub-tallec { color: var(--tallec-brown); }
  .sub-tallec .dot { background: var(--tallec-brown); }
</style>
</head>
<body>

  <section class="card card-back" aria-label="Card back">
    <div class="back-texture" role="img" aria-label="Embossed repeating brand pattern on black"></div>
    <div class="back-mark"><span class="mark-square"></span>VELSTRAND</div>
  </section>

  <section class="card card-front" aria-label="Card front">
    <div class="brand-block">
      <span class="mark-square"></span>
      <div class="brand-name">Velstrand<br>Group</div>
    </div>

    <div class="divider"></div>

    <div class="contact">
      <div class="person">Elias Varnum</div>
      <div class="role">Managing Director</div>
      <address>482 Tovey Lane<br>Regina, SK S7J 2B9</address>
      <ul>
        <li>
          <svg viewBox="0 0 24 24"><path d="M6.6 10.8a15.1 15.1 0 0 0 6.6 6.6l2.2-2.2a1 1 0 0 1 1-.25 11.4 11.4 0 0 0 3.6.57 1 1 0 0 1 1 1V20a1 1 0 0 1-1 1A17 17 0 0 1 3 4a1 1 0 0 1 1-1h3.5a1 1 0 0 1 1 1c0 1.25.2 2.45.57 3.57a1 1 0 0 1-.25 1z"/></svg>
          1.855.555.BILD (2453)
        </li>
        <li>
          <svg viewBox="0 0 24 24"><path d="M7 1h10a2 2 0 0 1 2 2v18a2 2 0 0 1-2 2H7a2 2 0 0 1-2-2V3a2 2 0 0 1 2-2zm0 3v14h10V4zm5 15.5a1 1 0 1 0 0 2 1 1 0 0 0 0-2z"/></svg>
          306.555.0147
        </li>
        <li>
          <svg viewBox="0 0 24 24"><path d="M2 5h20v14H2zm2 2v.5l8 5 8-5V7zm0 2.8V17h16V9.8l-8 5z"/></svg>
          elias@velstrandg.com
        </li>
        <li>
          <svg viewBox="0 0 24 24"><path d="M12 2a10 10 0 1 0 0 20 10 10 0 0 0 0-20zm6.9 6h-3a15 15 0 0 0-1.3-3.9A8 8 0 0 1 18.9 8zM12 4c.8 1.2 1.5 2.5 1.9 4h-3.8c.4-1.5 1.1-2.8 1.9-4zM4.3 14a8 8 0 0 1 0-4h3.4a16 16 0 0 0 0 4zm.8 2h3a15 15 0 0 0 1.3 3.9A8 8 0 0 1 5.1 16zm3-8h-3a8 8 0 0 1 4.3-3.9A15 15 0 0 0 8.1 8zM12 20c-.8-1.2-1.5-2.5-1.9-4h3.8c-.4 1.5-1.1 2.8-1.9 4zm2.3-6H9.7a14 14 0 0 1 0-4h4.6a14 14 0 0 1 0 4zm.3 5.9a15 15 0 0 0 1.3-3.9h3a8 8 0 0 1-4.3 3.9zm1.7-5.9a16 16 0 0 0 0-4h3.4a8 8 0 0 1 0 4z"/></svg>
          www <span class="web-accent">velstrandg</span>.com
        </li>
      </ul>
    </div>

    <div class="subsidiaries">
      <div class="subsidiary sub-copperline"><span class="dot"></span>Copperline</div>
      <div class="subsidiary sub-halvard"><span class="dot"></span>Halvard Sisters</div>
      <div class="subsidiary sub-tallec"><span class="dot"></span>Tallec</div>
    </div>
  </section>

</body>
</html>
```